KV MACHINERY DEPOT

we sell used heavy equipment look at our current website www.halvardhauling.com we are looking for a easier site to use with our new name

```html
<!DOCTYPE html>
<html lang="en">
<head>
<meta charset="utf-8">
<title>KV Machinery Depot – Used Heavy Equipment</title>
<link href="https://fonts.googleapis.com/css2?family=Figtree:wght@400;500;600;700&family=Inter:wght@400;500&display=swap" rel="stylesheet">
<style>
:root{
  --navy:#233b82;
  --gold:#a6874f;
  --gold-dark:#8f7140;
  --beige:#ebe2c9;
  --ink:#1b1b1b;
  --white:#ffffff;
}
*{box-sizing:border-box;margin:0;padding:0}
html,body{width:1200px;height:4062px;overflow:hidden}
body{position:relative;background:var(--white);font-family:"Figtree",sans-serif;color:var(--ink)}
.abs{position:absolute}
.topbar{left:0;top:0;width:1200px;height:80px;background:var(--navy)}
.topbar-cut{left:0;top:0;width:520px;height:80px}
.contact-chip{display:flex;align-items:center;gap:12px;color:var(--white);font-size:19px;top:18px}
.chip-icon{width:44px;height:44px;border-radius:50%;background:var(--white);display:flex;align-items:center;justify-content:center}
.brand{left:130px;top:80px;width:200px;height:100px;display:flex;align-items:center;gap:10px;font-weight:700;color:var(--navy);font-size:19px;line-height:1.1}
.brand-dot{width:18px;height:18px;border-radius:50%;background:var(--gold);flex:none}
.nav{top:113px;display:flex;gap:34px;left:417px;font-size:16px;font-weight:500}
.btn{display:flex;align-items:center;justify-content:center;color:var(--white);font-weight:500;font-size:16px}
.btn-gold{background:var(--gold)}
.btn-navy{background:var(--navy)}
.hero-photo{left:0;top:183px;width:1200px;height:640px;background:linear-gradient(180deg,#8e8c87 0%,#6f6a5e 35%,#8a7a52 70%,var(--gold) 100%)}
.hero-panel{left:0;top:318px;width:701px;height:404px;background:rgba(25,25,25,.72)}
.hero-title{left:132px;top:350px;width:520px;color:var(--white);font-size:41px;font-weight:700;line-height:1.24}
.hero-text{left:132px;top:517px;width:470px;color:var(--white);font-size:14.5px;line-height:1.65}
.advantages{left:0;top:820px;width:1200px;height:464px;background:var(--gold)}
.adv-title{left:132px;top:834px;width:620px;color:var(--white);font-size:27px;font-weight:500;line-height:1.3}
.adv-text{left:132px;top:918px;width:560px;color:var(--white);font-size:14px;line-height:1.7}
.feature{width:270px;display:flex;gap:14px;color:var(--white)}
.feature-icon{width:46px;height:46px;border-radius:50%;background:var(--white);flex:none;display:flex;align-items:center;justify-content:center}
.feature h4{font-size:13px;letter-spacing:1.6px;font-weight:600;line-height:1.3;text-transform:uppercase}
.feature p{font-size:12.5px;line-height:1.7;margin-top:7px;opacity:.95}
.finder{left:776px;top:729px;width:337px;height:428px;background:var(--white);box-shadow:0 4px 14px rgba(0,0,0,.18)}
.finder h3{position:absolute;left:31px;top:46px;color:var(--navy);font-size:22px;font-weight:600}
.field{position:absolute;height:41px;border:2px solid var(--gold);display:flex;align-items:center;gap:10px;padding:0 10px;color:#9e9e9e;font-size:13.5px}
.field .ic{width:24px;height:24px;border:1.5px solid #c9c9c9;border-radius:50%;flex:none}
.field .chev{margin-left:auto}
.search-btn{position:absolute;left:31px;top:346px;width:276px;height:37px}
.section-title{width:1200px;left:0;text-align:center;font-size:27px;font-weight:500;line-height:1.3}
.section-sub{width:1200px;left:0;text-align:center;font-size:13px;line-height:1.7}
.card{width:283px;height:422px;border-bottom-right-radius:50px;overflow:hidden;color:var(--white);text-align:center}
.card.navy{background:var(--navy)}
.card.gold{background:var(--gold)}
.card-photo{height:220px;background:linear-gradient(160deg,#b8c4d6 0%,#9a958a 45%,#6e6a62 100%)}
.card h3{font-size:20px;font-weight:500;line-height:1.25;margin-top:16px}
.card .price{font-size:30px;font-weight:500;margin-top:8px}
.card .pill{margin:26px auto 0;width:140px;height:38px;border-radius:19px;background:var(--white);display:flex;align-items:center;justify-content:center;font-size:15px}
.card.navy .pill{color:var(--navy)}
.card.gold .pill{color:var(--gold)}
.testimonial{width:293px;height:157px;background:var(--beige);border-top-right-radius:44px;font-family:"Inter",sans-serif;font-size:12.5px;line-height:1.6;padding:58px 18px 0}
.avatar{width:56px;height:56px;border-radius:50%;background:#b9b3a6;border:2px solid var(--white)}
.t-name{font-family:"Inter",sans-serif;font-size:12.5px;text-align:center;width:293px;line-height:1.9}
.cta{left:131px;top:3205px;width:966px;height:282px;border-radius:70px 40px 60px 70px;background:linear-gradient(135deg,#4a4844 0%,#5d5546 50%,#7b6a45 100%);overflow:hidden}
.cta-title{left:0;top:58px;width:966px;text-align:center;color:var(--white);font-size:27px;font-weight:500}
.cta-text{left:0;top:104px;width:966px;text-align:center;color:var(--white);font-size:14px;line-height:1.75}
.vline{width:2px;height:225px;background:var(--navy);top:3670px}
.footer-links{right:888px;top:3742px;text-align:right;color:var(--gold);font-size:12px;line-height:2.1}
.footer-links h4{color:var(--navy);font-size:15px;font-weight:500;margin-bottom:2px}
.footer-brand{left:380px;top:3700px;width:340px;text-align:center;color:var(--navy)}
.footer-contact{left:791px;top:3735px;color:var(--navy);font-size:12px;line-height:1.5;width:260px}
.footer-contact h4{color:var(--gold);font-size:15px;font-weight:500;margin-bottom:10px}
.fc-row{display:flex;gap:10px;margin-bottom:9px}
.social{left:497px;top:3900px;display:flex;gap:14px}
.social span{width:18px;height:18px;border-radius:50%;background:var(--navy);display:block}
.rule{left:104px;top:3965px;width:986px;height:1px;background:#555}
.legal{left:0;top:3997px;width:1200px;display:flex;justify-content:center;gap:16px;font-size:10.5px}
.legal a{color:var(--navy);text-decoration:underline}
</style>
</head>
<body>

<div class="abs topbar"></div>
<svg class="abs topbar-cut" viewBox="0 0 520 80" aria-hidden="true"><path d="M0 0H0V80H520C470 80 470 40 420 40H0Z" fill="#ffffff"/><path d="M0 40H420C470 40 470 80 520 80H0Z" fill="#ffffff"/></svg>
<div class="abs contact-chip" style="left:516px">
  <span class="chip-icon"><svg width="20" height="20" viewBox="0 0 24 24"><path d="M6.6 10.8a15 15 0 0 0 6.6 6.6l2.2-2.2c.3-.3.7-.4 1-.2 1.1.4 2.3.6 3.6.6.6 0 1 .4 1 1V20c0 .6-.4 1-1 1A17 17 0 0 1 3 4c0-.6.4-1 1-1h3.5c.6 0 1 .4 1 1 0 1.3.2 2.5.6 3.6.1.3 0 .7-.2 1z" fill="none" stroke="#a6874f" stroke-width="1.6"/></svg></span>619-555-0142
</div>
<div class="abs contact-chip" style="left:740px">
  <span class="chip-icon"><svg width="20" height="20" viewBox="0 0 24 24"><rect x="3" y="5" width="18" height="14" rx="2" fill="none" stroke="#a6874f" stroke-width="1.6"/><path d="M3 6l9 7 9-7" fill="none" stroke="#a6874f" stroke-width="1.6"/></svg></span>john@halvardhauling.com
</div>

<div class="abs brand"><span class="brand-dot"></span><span>KV MACHINERY DEPOT</span></div>
<nav class="abs nav"><span>Home</span><span>About Us</span><span>Equipment Sales</span><span>Financing Options</span></nav>
<div class="abs btn btn-gold" style="left:912px;top:103px;width:157px;height:44px">Apply Now</div>

<div class="abs hero-photo" role="img" aria-label="Yellow backhoe loader parked in an equipment yard"></div>
<div class="abs hero-panel"></div>
<h1 class="abs hero-title">Your Trusted Source For Heavy Equipment Nationwide</h1>
<p class="abs hero-text">We offer a wide range of used heavy construction equipment with the convenience of nationwide shipping. Plus, flexible financing options are available to help you get the equipment you need.</p>
<div class="abs btn btn-gold" style="left:132px;top:620px;width:157px;height:44px">Learn More</div>
<div class="abs btn btn-navy" style="left:307px;top:620px;width:157px;height:44px">Apply Now</div>

<div class="abs advantages"></div>
<div class="abs hero-photo" style="top:760px;height:60px;background:linear-gradient(180deg,rgba(166,135,79,0),var(--gold))"></div>
<h2 class="abs adv-title">Discover the unbeatable advantages of buying used heavy construction equipment today!</h2>
<p class="abs adv-text">At Halvard Hauling, we prioritise your needs by offering a wide selection of used heavy construction equipment. Our commitment is to ensure you find the right machinery efficiently and affordably.</p>

<div class="abs feature" style="left:132px;top:1040px"><span class="feature-icon"><svg width="24" height="24" viewBox="0 0 24 24"><circle cx="12" cy="12" r="8" fill="none" stroke="#a6874f" stroke-width="1.8"/><path d="M8 12l3 3 5-6" fill="none" stroke="#a6874f" stroke-width="1.8"/></svg></span><div><h4>Quality Equipment at Competitive Prices</h4><p>We offer top-notch used equipment without breaking the bank.</p></div></div>
<div class="abs feature" style="left:443px;top:1040px"><span class="feature-icon"><svg width="24" height="24" viewBox="0 0 24 24"><rect x="2" y="7" width="12" height="9" fill="none" stroke="#a6874f" stroke-width="1.8"/><path d="M14 10h4l3 3v3h-7" fill="none" stroke="#a6874f" stroke-width="1.8"/><circle cx="6" cy="18" r="2" fill="#a6874f"/><circle cx="17" cy="18" r="2" fill="#a6874f"/></svg></span><div><h4>Nationwide Shipping for Your Convenience</h4><p>We ship our equipment across the country, ensuring timely delivery to your location.</p></div></div>
<div class="abs feature" style="left:132px;top:1168px"><span class="feature-icon"><svg width="24" height="24" viewBox="0 0 24 24"><circle cx="12" cy="12" r="7" fill="none" stroke="#a6874f" stroke-width="1.8"/><path d="M12 8v8M9.5 10h4a1.5 1.5 0 0 1 0 3h-3a1.5 1.5 0 0 0 0 3h4" fill="none" stroke="#a6874f" stroke-width="1.5"/></svg></span><div><h4>Flexible Financing Options Available</h4><p>Our financing solutions are designed to fit your budget.</p></div></div>
<div class="abs feature" style="left:443px;top:1168px"><span class="feature-icon"><svg width="24" height="24" viewBox="0 0 24 24"><path d="M4 6h10l6 6-8 8-8-8z" fill="none" stroke="#a6874f" stroke-width="1.8"/><circle cx="8.5" cy="10" r="1.5" fill="#a6874f"/></svg></span><div><h4>Competitive Pricing for Every Budget</h4><p>Get the best value without compromising on quality.</p></div></div>

<div class="abs finder">
  <h3>Find The Right Equipment</h3>
  <div class="field" style="left:30px;top:107px;width:277px"><span class="ic"></span>Select Equipment<svg class="chev" width="12" height="12" viewBox="0 0 12 12"><path d="M2 4l4 4 4-4" fill="none" stroke="#666" stroke-width="1.5"/></svg></div>
  <div class="field" style="left:30px;top:160px;width:277px"><span class="ic"></span>Select Make<svg class="chev" width="12" height="12" viewBox="0 0 12 12"><path d="M2 4l4 4 4-4" fill="none" stroke="#666" stroke-width="1.5"/></svg></div>
  <div class="field" style="left:30px;top:214px;width:133px;padding:0 6px;gap:6px"><span class="ic" style="border-radius:4px"></span>Select Weight</div>
  <div class="field" style="left:174px;top:214px;width:133px;padding:0 6px;gap:6px"><span class="ic" style="border-radius:4px"></span>Select Year</div>
  <div class="field" style="left:30px;top:268px;width:277px">Enter Keyword</div>
  <div class="btn btn-navy search-btn"><svg width="16" height="16" viewBox="0 0 24 24" style="margin-right:8px"><circle cx="10" cy="10" r="6" fill="none" stroke="#fff" stroke-width="2.4"/><path d="M15 15l5 5" stroke="#fff" stroke-width="2.4"/></svg>Search</div>
</div>

<h2 class="abs section-title" style="top:1386px">Discover Our Featured Selection<br>of Quality Used Heavy Equipment</h2>
<p class="abs section-sub" style="top:1468px">Explore our carefully curated range of used heavy construction<br>equipment. We ensure quality and reliability in every purchase.</p>

<div class="abs card navy" style="left:135px;top:1553px"><div class="card-photo" role="img" aria-label="Compact excavator in an equipment yard"></div><h3>2014 Korvan<br>KD-40X Dozer</h3><div class="price">$92,779</div><div class="pill">View Details</div></div>
<div class="abs card gold" style="left:458px;top:1553px"><div class="card-photo" role="img" aria-label="White skid steer loader on pavement"></div><h3>2015 Bracken BK-600<br>skid steer</h3><div class="price">$92,779</div><div class="pill">View Details</div></div>
<div class="abs card navy" style="left:781px;top:1553px"><div class="card-photo" role="img" aria-label="Orange telehandler under a cloudy sky"></div><h3>2014 Skyreach<br>SR-1006 Telehandler</h3><div class="price">$92,779</div><div class="pill">View Details</div></div>

<div class="abs card gold" style="left:135px;top:2030px"><div class="card-photo" role="img" aria-label="Yellow backhoe loader parked in a lot"></div><h3>2016 Caldor CL-430<br>Backhoe</h3><div class="price">$92,779</div><div class="pill">View Details</div></div>
<div class="abs card navy" style="left:458px;top:2030px"><div class="card-photo" role="img" aria-label="Telehandler with forks raised"></div><h3>2013 Liftmark<br>LM-1100 Telehandler</h3><div class="price">$92,779</div><div class="pill">View Details</div></div>
<div class="abs card gold" style="left:781px;top:2030px"><div class="card-photo" role="img" aria-label="Yellow crawler dozer in a yard"></div><h3>2014 Korvan<br>KD-40X Dozer</h3><div class="price">$92,779</div><div class="pill">View Details</div></div>

<div class="abs btn btn-gold" style="left:521px;top:2502px;width:157px;height:47px">View All</div>

<h2 class="abs section-title" style="top:2652px">Client <span style="color:var(--navy)">Testimonials</span></h2>
<p class="abs section-sub" style="top:2697px;font-size:14px">Hear what our partners and industry experts have to say</p>

<div class="abs testimonial" style="left:132px;top:2775px">The equipment we purchased exceeded our expectations and arrived on time.</div>
<div class="abs testimonial" style="left:452px;top:2775px">Reliable service and great prices! We will definitely come back for more.</div>
<div class="abs testimonial" style="left:770px;top:2775px">Halvard Hauling made our equipment purchase a breeze. Highly recommended!</div>
<div class="abs avatar" role="img" aria-label="Client portrait" style="left:250px;top:2902px"></div>
<div class="abs avatar" role="img" aria-label="Client portrait" style="left:570px;top:2902px"></div>
<div class="abs avatar" role="img" aria-label="Client portrait" style="left:888px;top:2902px"></div>
<div class="abs t-name" style="left:132px;top:2962px">John Doe<br>CEO, XYZ Company</div>
<div class="abs t-name" style="left:452px;top:2962px">John Doe<br>CEO, XYZ Company</div>
<div class="abs t-name" style="left:770px;top:2962px">John Doe<br>CEO, XYZ Company</div>

<div class="abs cta" role="img" aria-label="Backhoe loaders parked in an equipment yard">
  <h2 class="abs cta-title">Explore Our Quality Equipment Today</h2>
  <p class="abs cta-text">Browse our extensive range of used heavy construction<br>equipment or contact our sales team for assistance.</p>
  <div class="abs btn" style="left:299px;top:180px;width:157px;height:42px;border:1.5px solid #fff">Browse</div>
  <div class="abs btn btn-gold" style="left:474px;top:180px;width:157px;height:42px">Apply Now</div>
</div>

<div class="abs vline" style="left:356px"></div>
<div class="abs vline" style="left:744px"></div>
<div class="abs footer-links"><h4>Quick Links</h4>Home<br>About Us<br>Equipment Sales<br>Financing Options</div>
<div class="abs footer-brand">
  <div style="display:flex;align-items:center;justify-content:center;gap:10px;margin-top:76px;white-space:nowrap"><span class="brand-dot" style="width:20px;height:20px"></span><span style="font-size:24px;font-weight:700;line-height:1.1">KV MACHINERY DEPOT</span></div>
  <div style="font-size:12px;letter-spacing:2px;margin-top:12px;color:var(--gold)">USED HEAVY EQUIPMENT SALES</div>
  <div style="font-size:11px;margin-top:4px">4820 RIDGELINE ROAD LAKESIDE CA 92040</div>
  <div style="font-size:13px;color:var(--gold);margin-top:2px;letter-spacing:1px">619-555-0142</div>
</div>
<div class="abs social"><span></span><span></span><span></span><span></span></div>
<div class="abs footer-contact">
  <h4>Contact Us</h4>
  <div class="fc-row"><svg width="14" height="14" viewBox="0 0 24 24"><path d="M6.6 10.8a15 15 0 0 0 6.6 6.6l2.2-2.2c.3-.3.7-.4 1-.2 1.1.4 2.3.6 3.6.6.6 0 1 .4 1 1V20c0 .6-.4 1-1 1A17 17 0 0 1 3 4c0-.6.4-1 1-1h3.5c.6 0 1 .4 1 1 0 1.3.2 2.5.6 3.6.1.3 0 .7-.2 1z" fill="#8f7140"/></svg>619-555-0142</div>
  <div class="fc-row"><svg width="14" height="14" viewBox="0 0 24 24"><rect x="2" y="5" width="20" height="14" rx="1" fill="#8f7140"/><path d="M2 6l10 7 10-7" fill="none" stroke="#fff" stroke-width="1.6"/></svg>john@halvardhauling.com</div>
  <div class="fc-row"><svg width="14" height="16" viewBox="0 0 24 28" style="flex:none"><path d="M12 0a9 9 0 0 0-9 9c0 7 9 17 9 17s9-10 9-17a9 9 0 0 0-9-9z" fill="#8f7140"/><circle cx="12" cy="9" r="3.5" fill="#fff"/></svg><span>Halvard Hauling Inc 4820<br>Ridgeline Road, Lakeside CA<br>92040</span></div>
</div>
<div class="abs rule"></div>
<div class="abs legal"><span>© 2024 Halvard Hauling. All rights reserved.</span><span style="width:20px"></span><a>Privacy Policy</a><a>Terms of Service</a><a>Cookies Settings</a></div>

</body>
</html>
```